Refresh of a rather different IT outfit website

Our web site is starting to show it's age. You can see the existing site here: www.plumbcorner.net. As a growing company we want to come across as a dynamic collection of IT experts.

We want to update the design so are open to any colour palette and look, but want to retain our current table logo. We use the logo on our business cards but with a white background - see the attached file, so you don't need to keep the brown or the green.

The design should consider the range of browsers that will be looking at the site - so please show how it will look on a wide screen laptop and a 768x1024 tablet.

We want to add some pages about our team and their skills, probably with photos of each person on the team.

This is an uncoded project - the PSD files of the design is required, not coding.
Updates

Thanks everyone for the submissions so far.  It's a holiday day in the UK today but we will get some feedback on the designs so far out to you.

Target Market(s)

Architects and other creative types looking for IT support

Industry/Entity Type

Business

Font styles to use
Serif
Sans Serif

Requirements
Must have
• Must look good on a laptop and an iPad.

```html
<!DOCTYPE html>
<html lang="en">
<head>
<meta charset="utf-8">
<title>plumbcorner — IT support</title>
<link href="https://fonts.googleapis.com/css2?family=Open+Sans:wght@400;600;700;800&display=swap" rel="stylesheet">
<style>
:root{
  --plum:#8c1a4f;
  --plum-dark:#6d1240;
  --ink:#333a40;
  --muted:#8a9096;
  --paper:#ffffff;
  --mist:#eceef1;
  --slate:#5b6167;
  --slate-line:#8d9399;
}
*{box-sizing:border-box;margin:0;padding:0}
html,body{width:855px;height:1200px;overflow:hidden;background:var(--paper)}
body{position:relative;font-family:"Open Sans",Arial,sans-serif;color:var(--ink)}
.abs{position:absolute}

/* header */
.site-header{left:0;top:0;width:855px;height:92px;background:var(--paper)}
.contact-strip{left:640px;top:6px;width:160px;height:18px;display:flex;gap:8px;align-items:center;font-size:7px;color:var(--paper)}
.contact-strip span{background:var(--plum);padding:3px 6px;white-space:nowrap}
.socials{left:700px;top:34px;display:flex;gap:6px}
.socials i{display:block;width:20px;height:20px;background:#c9ccd0}
.brand{left:100px;top:24px;font-weight:600;font-size:22px;color:var(--ink);letter-spacing:0}
.main-nav{left:100px;top:60px;display:flex;gap:22px;font-size:9px;color:var(--ink)}
.main-nav a{color:inherit;text-decoration:none;padding-bottom:4px}
.main-nav a.active{color:var(--plum);border-bottom:2px solid var(--plum);font-weight:600}

/* hero */
.hero{left:85px;top:94px;width:685px;height:292px;overflow:hidden}
.hero-photo{position:absolute;inset:0;background:linear-gradient(120deg,#e9c96a 0%,#bfa46a 30%,#c7c9cc 60%,#9fa3a8 100%)}
.hero svg{position:absolute;inset:0}
.hero-copy{position:absolute;left:448px;top:120px;width:225px;color:var(--paper)}
.hero-copy .kicker{font-size:10px}
.hero-copy h1{font-size:18px;font-weight:800;letter-spacing:.2px;margin:2px 0 10px;white-space:nowrap}
.hero-copy p{font-size:9px;line-height:1.5}
.hero-copy .btn{display:inline-block;margin-top:14px;border:1px solid var(--paper);padding:5px 10px;font-size:7px;font-weight:700;letter-spacing:.5px}

/* features */
.features{left:0;top:396px;width:855px;height:250px;background:var(--mist)}
.feature{top:412px;width:205px}
.feature h2{font-size:10px;font-weight:700;color:var(--ink);margin-bottom:6px}
.feature .tag{display:block;width:38px;height:2px;background:var(--plum);margin-bottom:8px}
.feature .media{height:72px;background:linear-gradient(135deg,#b9b0a6,#7e8790)}
.feature p{font-size:7px;line-height:1.6;color:var(--muted);margin-top:10px}
.services .media{position:relative;background:linear-gradient(135deg,#5e6f86,#c9ccd1)}
.services .media svg{position:absolute;left:88px;top:21px}
.blog .media{background:linear-gradient(135deg,#c9a48a,#6d7680)}
.blog .headline{background:var(--plum);color:var(--paper);padding:6px 8px;font-size:8px;font-weight:700;line-height:1.35}
.blog .headline small{display:block;font-weight:400;font-size:6px;margin-top:3px}

/* team */
.team-band{left:0;top:646px;width:855px;height:300px;background:var(--mist)}
.team-band svg{position:absolute;inset:0}
.team-title{left:100px;top:668px;font-size:11px;font-weight:700;color:var(--paper)}
.member{top:696px;width:155px;background:var(--paper);padding-bottom:10px}
.member .photo{height:128px}
.member h3{font-size:9px;font-weight:700;color:var(--plum);padding:9px 10px 1px}
.member .role{font-size:7px;color:var(--ink);padding:0 10px}
.member p{font-size:6.5px;line-height:1.55;color:var(--muted);padding:5px 10px 0}

/* customers */
.customers{left:0;top:950px;width:855px;height:215px;background:var(--slate);color:var(--paper)}
.customers h2{position:absolute;left:0;width:855px;top:24px;text-align:center;font-weight:400;font-size:20px}
.quote{position:absolute;left:150px;top:64px;width:555px;height:58px;border:1px solid var(--slate-line);display:flex;align-items:center;padding:0 14px;gap:20px}
.quote p{font-size:8px;line-height:1.55;flex:1}
.quote cite{font-style:normal;font-size:8px;font-weight:700;white-space:nowrap}
.quote cite small{display:block;font-weight:400;font-size:6px}
.clients{position:absolute;left:85px;top:150px;width:685px;display:flex;justify-content:space-between;align-items:center}
.clients span{display:flex;align-items:center;gap:5px;font-size:11px;font-weight:700;color:var(--paper)}
.clients span i{display:block;width:10px;height:10px;border-radius:50%;background:var(--paper)}

/* footer */
.site-footer{left:0;top:1165px;width:855px;height:35px;background:var(--paper);font-size:6.5px;color:var(--muted)}
.site-footer .copy{position:absolute;left:100px;top:14px}
.site-footer nav{position:absolute;right:100px;top:14px;display:flex;gap:16px}
</style>
</head>
<body>

<header class="abs site-header">
  <div class="abs contact-strip"><span>info@plumbcorner.net</span><span>+1 555 0134 210</span></div>
  <div class="abs socials"><i></i><i></i><i></i></div>
  <div class="abs brand">plumbcorner</div>
  <nav class="abs main-nav">
    <a class="active">Home</a><a>About</a><a>What We Do</a><a>News</a><a>Articles</a><a>Clients</a><a>Partners</a><a>Contact Us</a>
  </nav>
</header>

<section class="abs hero">
  <div class="hero-photo" role="img" aria-label="Upward view of a glass office tower against the sky"></div>
  <svg width="685" height="292" viewBox="0 0 685 292">
    <polygon points="360,0 685,0 685,292 240,292" fill="#8c1a4f" opacity=".88"/>
  </svg>
  <div class="hero-copy">
    <div class="kicker">Welcome to</div>
    <h1>EXCEED EXPECTATIONS</h1>
    <p>Creating the difference is our job. We love all the things we do. Our solutions are built to keep you running on superior quality.</p>
    <span class="btn">LEARN MORE</span>
  </div>
</section>

<div class="abs features"></div>

<article class="abs feature" style="left:85px">
  <h2>About Us</h2><span class="tag"></span>
  <div class="media" role="img" aria-label="Team of colleagues working together at a desk"></div>
  <p>Lorem ipsum dolor sit amet, consectetur adipiscing elit, sed do eiusmod tempor incididunt ut labore et dolore magna aliqua. Ut enim ad minim veniam.</p>
</article>

<article class="abs feature services" style="left:325px">
  <h2>Our Services</h2><span class="tag"></span>
  <div class="media" role="img" aria-label="Consultant presenting to a client">
    <svg width="30" height="30" viewBox="0 0 30 30"><circle cx="15" cy="15" r="15" fill="#8c1a4f"/><path d="M12 9l7 6-7 6" stroke="#fff" stroke-width="2" fill="none"/></svg>
  </div>
  <p>Lorem ipsum dolor sit amet, consectetur adipiscing elit, sed do eiusmod tempor incididunt ut labore et dolore magna aliqua. Ut enim ad minim veniam.</p>
</article>

<article class="abs feature blog" style="left:565px">
  <h2>From the Blog</h2><span class="tag"></span>
  <div class="media" style="height:40px" role="img" aria-label="Person reading on a laptop"></div>
  <div class="headline">Lorem ipsum dolor sit amet, consectetur adipiscing elit, sed do eiusmod<small>March 12, 2024</small></div>
  <p>Lorem ipsum dolor sit amet, consectetur adipiscing elit, sed do eiusmod tempor incididunt ut labore.</p>
</article>

<section class="abs team-band">
  <svg width="855" height="300" viewBox="0 0 855 300">
    <polygon points="0,0 520,0 0,300" fill="#8c1a4f"/>
  </svg>
</section>
<h2 class="abs team-title">Our Team</h2>

<article class="abs member" style="left:85px">
  <div class="photo" role="img" aria-label="Portrait of Hannah Pierce" style="background:linear-gradient(160deg,#d8c7b8,#8f7a6a)"></div>
  <h3>Hannah Pierce</h3><div class="role">IT Consultant</div>
  <p>Lorem ipsum dolor sit amet, consectetur adipiscing elit sed do eiusmod tempor.</p>
</article>
<article class="abs member" style="left:261px">
  <div class="photo" role="img" aria-label="Portrait of Owen Brandt" style="background:linear-gradient(160deg,#cfd3d8,#6d6560)"></div>
  <h3>Owen Brandt</h3><div class="role">Network Engineer</div>
  <p>Lorem ipsum dolor sit amet, consectetur adipiscing elit sed do eiusmod tempor.</p>
</article>
<article class="abs member" style="left:438px">
  <div class="photo" role="img" aria-label="Portrait of Mira Castell" style="background:linear-gradient(160deg,#e2d6cc,#8a6a55)"></div>
  <h3>Mira Castell</h3><div class="role">Support Lead</div>
  <p>Lorem ipsum dolor sit amet, consectetur adipiscing elit sed do eiusmod tempor.</p>
</article>
<article class="abs member" style="left:615px">
  <div class="photo" role="img" aria-label="Portrait of Felix Ward" style="background:linear-gradient(160deg,#d4d6d9,#7a6b60)"></div>
  <h3>Felix Ward</h3><div class="role">Systems Architect</div>
  <p>Lorem ipsum dolor sit amet, consectetur adipiscing elit sed do eiusmod tempor.</p>
</article>

<section class="abs customers">
  <h2>Our Happy Customers</h2>
  <blockquote class="quote">
    <p>“Duis facilisis, tortor eget pharetra eleifend, felis orci molestie risus, non bibendum lacus et sit amet ligula. Phasellus rutrum accumsan neque, sit amet imperdiet nisl. Donec condimentum gravida aliquam.”</p>
    <cite>Lee Harper<small>Swift Assist Co.</small></cite>
  </blockquote>
  <div class="clients">
    <span><i></i>Northvale</span>
    <span><i></i>Hue Works</span>
    <span>Brightnest</span>
    <span><i></i>Tandem</span>
    <span><i></i>Lumenor</span>
    <span>Cartway</span>
  </div>
</section>

<footer class="abs site-footer">
  <div class="copy">Copyright 2024 Plumbcorner. All Rights Reserved</div>
  <nav><span>Home</span><span>About</span><span>What We Do</span><span>News</span><span>Articles</span><span>Clients</span><span>Partners</span><span>Contact Us</span></nav>
</footer>

</body>
</html>
```